Brimela packaging design

I would like to re-design my Art work with different flavor ice cream on the containers and lids example: if the flavor is chocolate I would like to show one scoop of chocolate on the container. In the attach is one container that is an example of what I have in mind.

Target Market(s)

My products will be deliver to supermarkets and local convenient stores

Colors
f78f20
ffffff
f04a50

Requirements
Must have
• I prefer Gold around the rim of the lids and ice cream picture on top
Nice to have
• Since 2001 and going strong Or we have over a decade of experience of producing ice cream.

```html
<!DOCTYPE html>
<html lang="en">
<head>
<meta charset="utf-8">
<title>Brimela Rich Chocolate Ice Cream – Packaging</title>
<link rel="stylesheet" href="https://fonts.googleapis.com/css2?family=Questrial&display=swap">
<style>
  :root {
    --backdrop: #fdf3f3;
    --wrap-pink: #ee6b70;
    --wrap-pink-deep: #e2555c;
    --lid-pink: #e65a60;
    --lid-oval: #d94c53;
    --gold-light: #e9cf4a;
    --gold-mid: #c9a515;
    --gold-dark: #8f7208;
    --frame-red: #9c2330;
    --ink: #2b1a1a;
    --band: #2a2020;
    --white: #ffffff;
    --choc-light: #b07a5c;
    --choc-dark: #5a2f1d;
  }
  * { box-sizing: border-box; margin: 0; padding: 0; }
  html, body {
    width: 1200px; height: 1200px; overflow: hidden;
    background: var(--backdrop);
    font-family: "Questrial", "Century Gothic", sans-serif;
  }
  .canvas { position: relative; width: 1200px; height: 1200px; }
  .artwork { position: absolute; inset: 0; }
  .brand-name {
    position: absolute; color: var(--white);
    font-weight: 400; letter-spacing: 1px; line-height: 1;
  }
  .tagline-band {
    position: absolute; background: var(--band); color: var(--white);
    font-size: 15px; padding: 4px 10px; white-space: nowrap;
  }
  .flavour-title {
    position: absolute; color: var(--ink); font-size: 30px; letter-spacing: 0.5px;
  }
  /* lid */
  .lid .brand-name { left: 150px; top: 395px; font-size: 80px; }
  .lid .tagline-band { left: 250px; top: 485px; font-size: 13px; }
  /* container wrap */
  .wrap .flavour-title { left: 660px; top: 290px; }
  .wrap .brand-name { left: 660px; top: 345px; font-size: 120px; }
  .wrap .tagline-band { left: 820px; top: 480px; font-size: 17px; }
</style>
</head>
<body>
<main class="canvas">
  <svg class="artwork" width="1200" height="1200" viewBox="0 0 1200 1200">
    <defs>
      <linearGradient id="gold-rim" x1="0" y1="0" x2="1" y2="1">
        <stop offset="0" stop-color="var(--gold-light)"/>
        <stop offset="0.5" stop-color="var(--gold-mid)"/>
        <stop offset="1" stop-color="var(--gold-dark)"/>
      </linearGradient>
      <radialGradient id="scoop-tones" cx="0.4" cy="0.45" r="0.6">
        <stop offset="0" stop-color="var(--choc-light)"/>
        <stop offset="1" stop-color="var(--choc-dark)"/>
      </radialGradient>
    </defs>

    <!-- Lid -->
    <g class="lid-shape">
      <circle cx="310" cy="420" r="260" fill="url(#gold-rim)"/>
      <circle cx="310" cy="420" r="228" fill="var(--lid-pink)"/>
      <ellipse cx="310" cy="430" rx="185" ry="150" fill="var(--lid-oval)" stroke="var(--frame-red)" stroke-width="2"/>
      <circle cx="310" cy="300" r="62" fill="var(--white)"/>
      <circle cx="310" cy="300" r="52" fill="url(#scoop-tones)" role="img" aria-label="Photo of a scoop of chocolate ice cream"/>
    </g>

    <!-- Container wrap -->
    <g class="wrap-shape">
      <path d="M600 150 L1150 150 L1100 1090 L650 1090 Z" fill="var(--wrap-pink)"
            role="img" aria-label="Pink wrap with a tone-on-tone floral pattern"/>
      <path d="M600 150 L1150 150 L1147 200 L603 200 Z" fill="var(--wrap-pink-deep)"/>
      <circle cx="870" cy="820" r="235" fill="var(--white)" stroke="var(--frame-red)" stroke-width="6"/>
      <circle cx="870" cy="830" r="200" fill="url(#scoop-tones)" role="img" aria-label="Photo of a large scoop of chocolate ice cream"/>
    </g>
  </svg>

  <section class="lid">
    <div class="brand-name">Brimela</div>
    <div class="tagline-band">fresh and premium ice cream</div>
  </section>

  <section class="wrap">
    <h2 class="flavour-title">Rich Chocolate Ice Cream</h2>
    <div class="brand-name">Brimela</div>
    <div class="tagline-band">fresh and premium ice cream</div>
  </section>
</main>
</body>
</html>
```